Aerial photo/video drone company needs new business card

Aerial visual company who offers photos and video services via drones.

We are QVL certified and work in the real estate, insurance, construction, and film industries.

I'm looking for a clean, professional, maybe even edgy design, that will be a conversation starter when networking.

I've included our logo, current business card, and font.

Our current business card is decent; albeit, I'm looking for something more unique. If you folks provide good designs, I'll definitely guarantee payment (and I'm not opposed to tipping if the design is above and beyond).

Target Market(s)

Insurance companies, real estate agents, construction companies, advertising & other creative agencies, and filmmakers/producers.

Industry/Entity Type

Business

Contact Information for Business Card

Company name pronounced air-a-vee.

Font styles to use
Other font styles liked:
• Font was uploaded; that or similar; not opposed to other fonts if they work well with the design

Requirements
Must have
• Clearly prominent logo; my name and title; phone number; email address; web address; mentioned "QVL Certified" or similar; should indicate "Aerial visual"
Nice to have
• Watermark of logo or otherwise
Should not have
• Pictures of drones or scenic shots

```html
<!DOCTYPE html>
<html lang="en">
<head>
<meta charset="utf-8">
<title>Skyvane Business Card</title>
<link href="https://fonts.googleapis.com/css2?family=Sen:wght@400;700;800&family=Kumbh+Sans:wght@400;600;700&display=swap" rel="stylesheet">
<style>
  :root {
    --navy: #233656;
    --blue: #2a92d4;
    --blue-soft: #4aa3dc;
    --white: #ffffff;
    --watermark: #f0f0f1;
    --stage: #e7e4e0;
  }
  * { margin: 0; padding: 0; box-sizing: border-box; }
  html, body { width: 1200px; height: 1000px; overflow: hidden; }
  body { background: var(--stage); position: relative; font-family: "Kumbh Sans", sans-serif; }

  .card { position: absolute; left: 266px; width: 666px; height: 398px; overflow: hidden; }
  .card--front { top: 74px; background: var(--white); }
  .card--back { top: 533px; background: var(--blue); }

  .brand-dot { position: absolute; left: 398px; top: 106px; width: 56px; height: 56px; border-radius: 50%; background: var(--navy); }
  .card--front .brand-dot { left: 130px; top: 32px; }
  .brand-name {
    position: absolute; font-family: "Sen", sans-serif; font-weight: 700;
    letter-spacing: 1px; line-height: 1;
  }
  .card--front .brand-name { left: 30px; top: 98px; font-size: 66px; color: var(--navy); }

  .holder { position: absolute; right: 33px; top: 176px; text-align: right; }
  .holder__name { font-family: "Sen", sans-serif; font-weight: 700; font-size: 22px; color: var(--navy); }
  .holder__title { font-size: 16px; color: var(--blue); margin-top: 4px; letter-spacing: .3px; }
  .holder-bar { position: absolute; right: 0; top: 178px; width: 12px; height: 42px; background: var(--blue); }

  .certification { position: absolute; left: 32px; top: 200px; font-weight: 700; font-size: 16px; color: var(--navy); }
  .contacts { position: absolute; left: 32px; top: 230px; list-style: none; }
  .contacts li { display: flex; align-items: center; gap: 8px; font-size: 17px; color: var(--navy); height: 24px; }
  .contacts svg { width: 15px; height: 15px; fill: var(--blue); }
  .services { position: absolute; left: 32px; top: 310px; font-size: 15px; color: var(--navy); line-height: 19px; }

  .footer-band { position: absolute; left: 0; bottom: 0; width: 666px; height: 33px; }
  .social { position: absolute; left: 30px; bottom: 8px; display: flex; align-items: center; gap: 6px; color: var(--white); font-size: 15px; }
  .social__dot { width: 18px; height: 18px; border-radius: 50%; background: var(--white); }
  .social__handle { margin-left: 4px; }

  .pattern-field { position: absolute; inset: 0; background: linear-gradient(135deg, #3b9ad8, #2a92d4 55%, #3a9bd9); }
  .card--back .brand-name { right: 48px; top: 250px; font-size: 94px; color: var(--white); }
  .card--back .brand-dot { left: 408px; top: 156px; width: 78px; height: 78px; background: var(--white); }
</style>
</head>
<body>
  <section class="card card--front" aria-label="Business card front">
    <div class="brand-dot"></div>
    <div class="brand-name">skyvane</div>

    <div class="holder-bar"></div>
    <div class="holder">
      <div class="holder__name">Daniel T. Marsh</div>
      <div class="holder__title">Owner / sUAS Pilot</div>
    </div>

    <div class="certification">QVL Certified</div>
    <ul class="contacts">
      <li><svg viewBox="0 0 16 16"><path d="M1 5c0-2 2-3 7-3s7 1 7 3v1h-4V4.5H5V6H1zM3 7h10l2 7H1z"/></svg>555.314.2790</li>
      <li><svg viewBox="0 0 16 16"><path d="M1 3h14v10H1zM2 4l6 5 6-5v-.2H2z" fill-rule="evenodd"/></svg>dan@skyvane.com</li>
      <li><svg viewBox="0 0 16 16"><circle cx="8" cy="8" r="7"/><path d="M1 8h14M8 1c3 3 3 11 0 14M8 1c-3 3-3 11 0 14" stroke="#fff" stroke-width="1" fill="none"/></svg>www.skyvane.com</li>
    </ul>
    <p class="services">Aerial Visual for<br>Real Estate - Insurance - Contruction - Film</p>

    <svg class="footer-band" viewBox="0 0 666 33" aria-hidden="true">
      <polygon points="0,0 395,0 376,33 0,33" fill="var(--navy)"/>
      <polygon points="401,0 666,0 666,33 382,33" fill="var(--blue)"/>
    </svg>
    <div class="social">
      <span class="social__dot"></span><span class="social__dot"></span><span class="social__dot"></span>
      <span class="social__handle">@skyvane</span>
    </div>
  </section>

  <section class="card card--back" aria-label="Business card back">
    <div class="pattern-field" role="img" aria-label="Repeating brand pattern in light blue tones"></div>
    <div class="brand-dot"></div>
    <div class="brand-name">skyvane</div>
  </section>
</body>
</html>
```